A new company focused on starting and investing in transformative businesses.

We need a simple and clean website with a few pages. we like larkmeadow.com as a starting point. we want the landing page to be very simple with an option to click through on the top right into INVESTOR LOGIN. then we want to be able to scroll down to see more about our company.

Target Market(s)

professional

Coding

Coded - Design and coding required

Number of Pages Required

2 page

Font styles to use
Serif
Sans Serif

Requirements
Must have
• HALVERN BUILDERS logo (attached as a file) on the top with INVESTOR LOGIN as a click through on the right. Please model the click through from larkmeadow.com. The description (also written in attached file) should be on the landing page. we do not want to have to scroll to read the description.

Then we can scroll down to read more about Halvern including the mission and the two types of businesses. More is detailed on the attached file called "Halvern Website Syntax"
Should not have
• should not be slow loading with lots of fancy graphics. should not be busy and with too many colors.

```html
<!DOCTYPE html>
<html lang="en">
<head>
<meta charset="utf-8">
<title>Halvern Builders</title>
<link rel="stylesheet" href="https://fonts.googleapis.com/css2?family=Lora:wght@400;500&display=swap">
<style>
  :root {
    --blue: #0d5aa0;
    --page-bg: #f2f2f2;
    --outer-bg: #ffffff;
    --ink: #222222;
    --muted: #9a9a9a;
    --subhead: #555555;
    --footer-bg: #adc9de;
    --photo-dark: #1a4f8c;
    --photo-light: #c4d8ea;
  }
  * { margin: 0; padding: 0; box-sizing: border-box; }
  html, body {
    width: 1200px; height: 1200px; overflow: hidden;
    background: var(--outer-bg);
    font-family: "Lora", Georgia, serif;
    color: var(--ink);
  }
  .page {
    position: absolute; left: 134px; top: 0;
    width: 932px; height: 1200px;
    background: var(--page-bg);
  }
  .brand {
    position: absolute; display: flex; align-items: center; gap: 8px;
    font-weight: 500; color: var(--blue); letter-spacing: 0.04em;
    line-height: 1.1;
  }
  .brand-mark { background: var(--blue); flex: none; }
  .site-header .brand { left: 96px; top: 16px; font-size: 16px; }
  .site-header .brand-mark { width: 30px; height: 30px; }
  .hero-bracket {
    position: absolute; left: 96px; top: 126px;
    width: 115px; height: 188px;
    border-left: 13px solid var(--blue);
    border-top: 16px solid var(--blue);
    border-top-right-radius: 8px;
  }
  .hero-statement {
    position: absolute; left: 130px; top: 155px; width: 440px;
    font-size: 30px; line-height: 39px; font-weight: 400;
  }
  .accent { color: var(--blue); }
  .scroll-cue { position: absolute; left: 328px; top: 372px; }
  .hero-photo {
    position: absolute; left: 584px; top: 41px;
    width: 306px; height: 477px; border-radius: 14px;
    background: linear-gradient(160deg, var(--photo-dark) 0%, #4f82b9 45%, var(--photo-light) 70%, #13406f 100%);
  }
  .mission {
    position: absolute; left: 137px; top: 632px; width: 680px;
    font-size: 25px; line-height: 37px;
  }
  .focus-area { position: absolute; top: 757px; width: 356px; }
  .focus-area.ground-up { left: 96px; }
  .focus-area.special { left: 476px; }
  .focus-area h2 {
    font-size: 17px; font-weight: 400; color: var(--subhead);
    letter-spacing: 0.02em; margin-bottom: 8px;
  }
  .focus-area p { font-size: 17.5px; line-height: 26.6px; color: var(--muted); }
  .site-footer {
    position: absolute; left: 0; top: 1055px; width: 932px; height: 145px;
    background: var(--footer-bg);
  }
  .site-footer .brand { left: 96px; top: 29px; font-size: 13px; }
  .site-footer .brand-mark { width: 24px; height: 24px; }
  .address {
    position: absolute; left: 96px; top: 78px;
    font-size: 12px; line-height: 14px; font-style: normal;
  }
  .copyright { position: absolute; left: 358px; top: 30px; font-size: 18px; }
  .media-contact {
    position: absolute; left: 358px; top: 78px;
    font-size: 12px; line-height: 14px;
  }
  .media-contact a { color: var(--blue); text-decoration: none; }
  .investor-login {
    position: absolute; left: 719px; top: 30px;
    font-size: 17px; color: var(--blue); text-decoration: none;
  }
</style>
</head>
<body>
<div class="page">
  <header class="site-header">
    <div class="brand"><span class="brand-mark"></span><span>HALVERN<br>BUILDERS</span></div>
  </header>

  <section class="hero">
    <div class="hero-bracket"></div>
    <h1 class="hero-statement"><span class="accent">Halvern Builders</span> is an entrepreneurial firm focused on building and growing transformational companies</h1>
    <svg class="scroll-cue" width="16" height="28" viewBox="0 0 16 28" aria-hidden="true">
      <line x1="8" y1="2" x2="8" y2="25" stroke="#0d5aa0" stroke-width="2"/>
      <polyline points="3,20 8,26 13,20" fill="none" stroke="#0d5aa0" stroke-width="2"/>
    </svg>
    <div class="hero-photo" role="img" aria-label="Upward view of curving glass skyscrapers in blue tones"></div>
  </section>

  <section class="about">
    <p class="mission">Our mission is to build <span class="accent">meaningful</span> businesses that create <span class="accent">enduring</span> value by impacting people in a <span class="accent">measurable</span> way.</p>
    <div class="focus-area ground-up">
      <h2>GROUND UP</h2>
      <p>Our ground up business applies a proven analytic process to identify value edge, a form of competitive advantage. We architect transformational companies and are deliberate in creating the foundation necessary to lead an industry.</p>
    </div>
    <div class="focus-area special">
      <h2>SPECIAL OPPORTUNITIES</h2>
      <p>We partner with exceptional teams that create value by transforming lives. Our investment focus includes large companies and spin-outs.</p>
    </div>
  </section>

  <footer class="site-footer">
    <div class="brand"><span class="brand-mark"></span><span>HALVERN<br>BUILDERS</span></div>
    <address class="address">4870 Alder Avenue<br>Portland, OR 97205</address>
    <p class="copyright">© 2021 Halvern Builders</p>
    <p class="media-contact">For media inquiries, please contact<br><a href="#">press@halvernbuilders.com</a></p>
    <a class="investor-login" href="#">Investor Login</a>
  </footer>
</div>
</body>
</html>
```